B2B IT project concept needs a website design for product (sales) pages

We need a website design, to attract customers to buy our services.

We dont yet have a name for our concept / if you have a great idea, feel free to be creative.

The design should communicate state of the art, professional, innovative and trustworthiness.

Technical requirements:
Format of delivery is HTML5 and CSS,.
The design is expected to be based on a well know CSS framework, like Bootstrap, or similar.

Our Concept
We are building a platform, by the means of which we can crowdsource quality inspection, from the design to delivery, to avoid the next IT disaster.

Our concept is a B2B product
Our customer base is large scale IT projects - typically public funding
The motivation for buying our product is : risk mitigation and avoiding failure (crashed, abandoned, never deployed, to full of errors, slow, dinosaurs) … see more here> http://www.bytegazette.co.uk/ctg/feature/5817394/the-10-worst-ever-government-it-projects

We define structure and guidelines. If the project follows these guidelines we guarantee delivery on deadlines
Our product is composed of the 4 steps below. Each can be purchased separately, or as a single insurance package.

The product is composed of 4 modules:
Module One: Why are we building this?
define project goals (research shows that 20% die because of this root cause)
stakeholder analysis
success criteria
minimal viable product definition
Module 2: What are we building ?
requirements specification & automated acceptance tests (research shows that 30% die because of this). Grades for req specification, and offer of help to improve. Review of req spec & grading is quite cheap (about 5.000 euro) - we see this as a sales channel
Module 3 : how are we building?
measuring during project execution
we set up measuring points in the continuous delivery process, and track that the developed product is inside quality margins (!)
module 4: navigate back on track
early warning system
warnings are deployed if irregularities are detected. failure to act on early warning voids the software delivery guarantee.

Target Market(s)

Our customer base is decision makers/sponsors of large scale IT projects - typically public funding

Industry/Entity Type

Software

Coding

Coded - Design and coding required

Number of Pages Required

1 page

Font styles to use
Sans Serif

Requirements
Must have
• Product description
• Contact form
• Packages of the service to select and inquire about
• should work on mobile platforms as well
Should not have
• payment options

```html
<!DOCTYPE html>
<html lang="en">
<head>
<meta charset="utf-8">
<title>Nordvik IT</title>
<link href="https://fonts.googleapis.com/css2?family=Open+Sans:wght@400;600&family=Roboto:wght@300;400&display=swap" rel="stylesheet">
<style>
:root{
  --blue:#0b87c8;
  --button:#3576c4;
  --title-blue:#3a7fc8;
  --ink:#333a40;
  --nav:#5b6369;
  --footer-bg:#f2f3f4;
  --white:#ffffff;
}
*{box-sizing:border-box;margin:0;padding:0}
html,body{width:990px;height:1200px;overflow:hidden}
body{position:relative;background:var(--white);font-family:"Open Sans",Arial,sans-serif;color:var(--ink)}
.abs{position:absolute}

/* header */
.site-header{left:0;top:0;width:990px;height:72px;background:var(--white);box-shadow:0 1px 3px rgba(0,0,0,.12);z-index:2}
.brand{left:80px;top:18px;font-size:28px;line-height:36px;color:var(--blue);font-weight:400}
.main-nav{right:60px;top:22px;display:flex;height:36px}
.main-nav a{display:block;padding:0 20px;line-height:28px;font-size:13px;color:var(--nav);text-decoration:none;border-left:1px solid #eceeef}
.main-nav a:first-child{border-left:none}
.main-nav a.active{color:var(--blue)}

/* hero */
.hero{left:0;top:72px;width:990px;height:470px}
.hero-photo{position:absolute;inset:0;background:radial-gradient(ellipse at 62% 45%,#e8d1c6 0%,#b9aeb0 30%,#7d7f8c 60%,#5f6574 100%),#8a8d98}
.hero-photo::after{content:"";position:absolute;inset:0;background:linear-gradient(90deg,rgba(240,238,236,.92) 0%,rgba(235,233,232,.7) 35%,rgba(255,255,255,0) 60%)}
.mission{left:104px;top:162px;width:310px}
.mission h1{font-family:"Roboto",Arial,sans-serif;font-weight:400;font-size:35px;line-height:40px;color:var(--title-blue)}
.mission p{margin-top:6px;font-size:10.6px;line-height:18.5px;color:#4a4f55}
.btn-more{display:inline-block;margin-top:15px;width:143px;height:37px;line-height:37px;text-align:center;background:var(--button);color:var(--white);font-size:14px;border-radius:2px;box-shadow:0 2px 3px rgba(0,0,0,.25)}
.slider-arrow{top:231px}

/* products */
.products{left:0;top:542px;width:990px;height:410px;background:var(--blue)}
.products h2{position:absolute;left:0;width:990px;top:55px;text-align:center;font-family:"Roboto",Arial,sans-serif;font-weight:400;font-size:26px;color:var(--white)}
.products .rule{left:465px;top:96px;width:60px;height:2px;background:var(--white)}
.card{top:170px;width:195px;height:180px;background:#e6f0f7;text-align:center;padding:44px 10px 0;box-shadow:0 3px 3px rgba(0,0,0,.12)}
.card.first{background:#f7f8f9}
.card h3{font-family:"Roboto",Arial,sans-serif;font-weight:300;font-size:15.5px;color:#3c4247;line-height:22px;white-space:nowrap}
.card p{margin-top:6px;font-size:9.2px;line-height:17px;color:#474d52}
.card-icon{top:132px;width:78px;height:78px;border-radius:50%;background:var(--blue);border:4px solid var(--white);display:flex;align-items:center;justify-content:center}

/* footer */
.site-footer{left:0;top:952px;width:990px;height:202px;background:var(--footer-bg)}
.footer-brand{left:80px;top:70px;font-size:22px;color:var(--blue)}
.col-title{font-family:"Roboto",Arial,sans-serif;font-size:13px;font-weight:400;color:#2c3237}
.col-title span{color:var(--blue)}
.info{left:252px;top:27px}
.info ul{list-style:none;margin-top:10px}
.info li{font-size:9.4px;line-height:21.3px;color:#3e4449}
.newsletter{left:439px;top:27px;width:218px;height:150px}
.newsletter p{margin-top:9px;font-size:9.4px;line-height:16px;color:#3e4449}
.field{position:absolute;left:0;height:35px;background:var(--white);border:1px solid #dfe2e4;font-size:9.4px;line-height:33px;padding-left:11px;color:#4a5055}
.field-name{top:68px;width:218px}
.field-email{top:111px;width:137px}
.subscribe{position:absolute;left:137px;top:111px;width:81px;height:35px;background:var(--blue);color:var(--white);font-size:11px;line-height:35px;text-align:center}
.contact{left:747px;top:27px}
.contact address{margin-top:8px;font-style:normal;font-size:10.5px;line-height:16.3px;color:#4a5055}
.contact-line{display:flex;align-items:center;gap:10px;font-size:10.5px;color:#2f3539;margin-top:6px}
.contact-line:first-of-type{margin-top:14px}

.bottom-bar{left:0;top:1154px;width:990px;height:46px;background:var(--blue)}
.copyright{left:82px;top:16px;font-size:9.4px;color:var(--white)}
.social{left:810px;top:13px;display:flex;gap:6px}
.social span{width:20px;height:20px;border-radius:50%;background:var(--white)}
</style>
</head>
<body>

<header class="abs site-header">
  <div class="abs brand">Nordvik IT</div>
  <nav class="abs main-nav">
    <a class="active" href="#">Home</a>
    <a href="#">Who We Are</a>
    <a href="#">Our Services</a>
    <a href="#">News</a>
    <a href="#">Contact us</a>
  </nav>
</header>

<section class="abs hero">
  <div class="hero-photo" role="img" aria-label="Businessman in a suit holding up a glowing B2B emblem between his fingers"></div>
  <div class="abs mission">
    <h1>OUR MISSION</h1>
    <p>Nemo enim ipsam voluptatem quia voluptas sit aspernatur aut odit aut fugit, sed quia consequuntur magni dolores eos qui ratione voluptatem sequi nesciunt. Neque porro</p>
    <span class="btn-more">More Information</span>
  </div>
  <svg class="abs slider-arrow" style="left:27px" width="29" height="29" viewBox="0 0 29 29"><circle cx="14.5" cy="14.5" r="14.5" fill="#8d8f93" opacity=".75"/><path d="M16.5 8.5l-6 6 6 6" stroke="#fff" stroke-width="2" fill="none"/></svg>
  <svg class="abs slider-arrow" style="left:939px" width="29" height="29" viewBox="0 0 29 29"><circle cx="14.5" cy="14.5" r="14.5" fill="#4a4e5a" opacity=".75"/><path d="M12.5 8.5l6 6-6 6" stroke="#fff" stroke-width="2" fill="none"/></svg>
</section>

<section class="abs products">
  <h2>OUR PRODUCTS</h2>
  <div class="abs rule"></div>

  <article class="abs card first" style="left:76px">
    <h3>Why are we building this?</h3>
    <p>define project goals (research shows that 20% die because of this root cause) stakeholder analysis success criteria minimal viable product definition</p>
  </article>
  <article class="abs card" style="left:286px">
    <h3>What are we building ?</h3>
    <p>requirements specification &amp; automated acceptance tests (research shows that 30% die because of this). Grades for req specification, and offer of help to improve.</p>
  </article>
  <article class="abs card" style="left:498px">
    <h3>How are we building?</h3>
    <p>measuring during project execution we set up measuring points in the continuous delivery process, and track that the developed product is inside quality margins</p>
  </article>
  <article class="abs card" style="left:709px">
    <h3>Navigate back on track</h3>
    <p>Early warning system<br>warnings are deployed if irregularities are detected. failure to act on early warning voids the software delivery guarantee.</p>
  </article>

  <div class="abs card-icon" style="left:134px">
    <svg width="28" height="30" viewBox="0 0 28 30"><circle cx="14" cy="8" r="7" fill="#fff"/><path d="M1 29c0-9 5-12 13-12s13 3 13 12z" fill="#fff"/></svg>
  </div>
  <div class="abs card-icon" style="left:345px">
    <svg width="34" height="30" viewBox="0 0 34 30"><path d="M2 2h12l14 14-11 11L2 13z" fill="#fff"/><circle cx="8" cy="8" r="2.5" fill="#0b87c8"/><path d="M18 2h3l14 14-11 11-1.5-1.5 9.5-9.5z" fill="#fff"/></svg>
  </div>
  <div class="abs card-icon" style="left:557px">
    <svg width="24" height="32" viewBox="0 0 24 32"><rect x="2" y="1" width="20" height="30" fill="none" stroke="#fff" stroke-width="2"/><g fill="#fff"><rect x="6" y="5" width="3" height="3"/><rect x="11" y="5" width="3" height="3"/><rect x="16" y="5" width="3" height="3"/><rect x="6" y="11" width="3" height="3"/><rect x="11" y="11" width="3" height="3"/><rect x="16" y="11" width="3" height="3"/><rect x="6" y="17" width="3" height="3"/><rect x="11" y="17" width="3" height="3"/><rect x="16" y="17" width="3" height="3"/><rect x="10" y="24" width="5" height="7"/></g></svg>
  </div>
  <div class="abs card-icon" style="left:768px">
    <svg width="30" height="30" viewBox="0 0 30 30"><path d="M28 2L2 13l10 4 4 11z" fill="none" stroke="#fff" stroke-width="2.4" stroke-linejoin="round"/><path d="M28 2L12 17" stroke="#fff" stroke-width="2.4"/></svg>
  </div>
</section>

<footer class="abs site-footer">
  <div class="abs footer-brand">Nordvik IT</div>

  <div class="abs info">
    <h4 class="col-title">INFORMATION</h4>
    <ul>
      <li>Home</li>
      <li>Who We Are</li>
      <li>Our Products</li>
      <li>News</li>
      <li>Contact</li>
    </ul>
  </div>

  <div class="abs newsletter">
    <h4 class="col-title">SIGN UP FOR <span>NEWSLETTER</span></h4>
    <p>Join us today and start celebrate the life of your lost loved one.</p>
    <div class="field field-name">Enter Name</div>
    <div class="field field-email">Enter Email</div>
    <div class="subscribe">SUBSCRIBE</div>
  </div>

  <div class="abs contact">
    <h4 class="col-title">CONTACT US</h4>
    <address>Nordvik IT<br>18 Harbor Row, Suite 402,<br>Lakeview, IL 60990, United States</address>
    <div class="contact-line">
      <svg width="16" height="16" viewBox="0 0 16 16"><path d="M4 1l3 4-2 2c1 2 2 3 4 4l2-2 4 3-2 3C7 15 1 9 1 3z" fill="none" stroke="#0b87c8" stroke-width="1.2" stroke-linejoin="round"/></svg>
      +1.555.014.2290
    </div>
    <div class="contact-line">
      <svg width="16" height="12" viewBox="0 0 16 12"><rect x=".6" y=".6" width="14.8" height="10.8" fill="none" stroke="#0b87c8" stroke-width="1.2"/><path d="M1 1l7 6 7-6M1 11l5-5M15 11l-5-5" fill="none" stroke="#0b87c8" stroke-width="1.2"/></svg>
      info@nordvikit.com
    </div>
  </div>
</footer>

<div class="abs bottom-bar">
  <div class="abs copyright">© 2016 Nordvik IT | All Rights Reserved</div>
  <div class="abs social"><span></span><span></span><span></span><span></span></div>
</div>

</body>
</html>
```